Meridane Haulage - Website

A clean, not cluttered informative website for our business. We specialize in the transportation of radioactive materials across North America. The site is mostly for information about our company and will not be used to attract business but will be used to attract employee's mainly drivers. Driver's are very hard to find in our area. One of the pages needs to be a job's posting page with an apply now button. Either an application can be filled out there or a resume can be uploaded which ever functionality works better. I would like a website that I can easily edit, ability to change text and photos.

Number of Pages Required

5+ page

Colors

Designer to choose colors to be used in the design.

Requirements
Must have
• Home - About - Services - Jobs - Contact pages
• A way prospective employee's can apply or upload their resume to be emailed to me
• Very clean apperance
Should not have
• I don't want it to be busy

```html
<!DOCTYPE html>
<html lang="en">
<head>
<meta charset="utf-8">
<title>Meridane Haulage</title>
<link href="https://fonts.googleapis.com/css2?family=Rajdhani:wght@300;400;500;600;700&display=swap" rel="stylesheet">
<style>
:root{
  --red:#e31b23;
  --blue:#0b4a84;
  --ink:#222;
  --grey:#7a7a7a;
  --light:#efefef;
  --footer:#111;
  --white:#fff;
}
*{box-sizing:border-box;margin:0;padding:0}
html,body{width:1200px;height:2908px;overflow:hidden}
body{position:relative;font-family:'Rajdhani',sans-serif;color:var(--ink);background:var(--white)}
.abs{position:absolute}
.btn{position:absolute;display:flex;align-items:center;justify-content:center;background:var(--red);color:var(--white);font-weight:700;font-size:12px;letter-spacing:.3px;text-transform:uppercase}

/* header */
.header{left:0;top:0;width:1200px;height:70px;background:var(--white)}
.brand{position:absolute;left:94px;top:16px;font-weight:700;font-size:28px;color:var(--red);line-height:1;letter-spacing:1px;text-transform:uppercase}
.brand small{display:block;font-size:12px;letter-spacing:9px;color:var(--ink);margin-top:2px}
.nav a{position:absolute;top:26px;font-size:14px;font-weight:500;color:var(--ink);text-decoration:none}
.nav a.active{color:var(--red)}

/* hero */
.hero{left:0;top:70px;width:1200px;height:566px;background:linear-gradient(100deg,#4b5257 0%,#2f3a3c 45%,#1c2a2a 70%,#263532 100%)}
.hero-text{right:94px;top:304px;text-align:right;color:var(--white)}
.hero-text .lead{font-size:48px;font-weight:300;line-height:53px;white-space:nowrap}
.hero-text h1{font-size:60px;font-weight:700;line-height:52px;white-space:nowrap}
.hero-text h1 span{color:var(--red)}
.dots span{position:absolute;top:602px;width:10px;height:10px;border-radius:50%;background:#777}
.dots span.on{background:var(--red)}

/* intro */
.intro{left:185px;top:692px;width:830px;text-align:center;font-size:11.5px;line-height:22px;color:var(--grey)}

/* who we are */
.who{left:0;top:812px;width:542px;height:442px;background:var(--blue);color:var(--white)}
.who h2{position:absolute;left:90px;top:114px;font-size:31px;font-weight:500}
.who p{position:absolute;left:92px;top:172px;width:420px;font-size:12px;line-height:20px}
.photo{position:absolute}

/* jobs */
.jobs{left:0;top:1254px;width:1200px;height:602px;background:linear-gradient(180deg,#3c4f68 0%,#5f6f82 40%,#2a2b2d 80%,#0e0e0e 100%)}
.jobs-text{left:90px;top:1684px;width:560px;color:var(--white)}
.jobs-text h2{font-size:32px;font-weight:700;line-height:1}
.jobs-text p{margin-top:12px;font-size:13px;line-height:22px}
.apply{left:694px;top:1293px;width:412px;height:523px;background:var(--red);border:2px solid var(--white)}
.apply h3{position:absolute;left:66px;top:24px;color:var(--white);font-size:25px;font-weight:500}
.field{position:absolute;height:38px;background:var(--white);font-size:11px;color:#555;display:flex;align-items:center;padding-left:8px}
.field.select{justify-content:space-between;padding-right:10px}
.caret{width:0;height:0;border-left:4px solid transparent;border-right:4px solid transparent;border-top:5px solid #333}
.upload{background:transparent;border:1px solid var(--white)}
.submit{background:#222}

/* services */
.services{left:0;top:1856px;width:1200px;height:572px;background:var(--light)}
.card{position:absolute;top:1940px;width:320px;text-align:center}
.card .circle{width:226px;height:226px;border-radius:50%;margin:0 auto}
.card h3{margin-top:20px;font-size:18px;font-weight:700;color:#333}
.card p{margin-top:6px;font-size:12.5px;line-height:20px;color:var(--grey)}

/* footer */
.footer{left:0;top:2428px;width:1200px;height:480px;background:var(--footer);color:var(--white)}
.f-brand{position:absolute;left:90px;top:84px;font-weight:700;font-size:28px;line-height:1;letter-spacing:1px;text-transform:uppercase}
.f-brand small{display:block;font-size:12px;letter-spacing:9px;margin-top:2px}
.f-about{position:absolute;left:90px;top:160px;width:250px;font-size:12.5px;line-height:21px}
.f-title{position:absolute;top:84px;font-size:21px;font-weight:500}
.f-links a{position:absolute;left:424px;font-size:12.5px;color:var(--white);text-decoration:none}
.f-contact{position:absolute;left:597px;font-size:12.5px;line-height:20px}
.f-contact b{font-weight:700}
.f-news{position:absolute;left:838px;top:150px;width:260px;font-size:12.5px;line-height:21px}
.f-input{position:absolute;left:838px;top:208px;width:268px;height:44px;background:var(--white);color:#666;font-size:12px;display:flex;align-items:center;padding-left:16px}
.social span{position:absolute;top:337px;width:26px;height:26px;border-radius:50%;background:var(--white)}
.copy{position:absolute;left:0;top:416px;width:1200px;text-align:center;font-size:11px}
.copy span{color:var(--red)}
</style>
</head>
<body>

<header class="abs header">
  <div class="brand">Meridane<small>Haulage</small></div>
  <nav class="nav">
    <a class="active" style="left:752px" href="#">Home</a>
    <a style="left:828px" href="#">About</a>
    <a style="left:905px" href="#">Services</a>
    <a style="left:996px" href="#">Jobs</a>
    <a style="left:1064px" href="#">Contact</a>
  </nav>
</header>

<section class="abs hero" role="img" aria-label="Grey semi truck hauling a flatbed of marked drums beside a brick building"></section>
<div class="abs hero-text">
  <div class="lead">We are Specialize</div>
  <h1>The <span>Transportation</span> of<br>Radoactive materials</h1>
</div>
<div class="btn" style="left:985px;top:482px;width:122px;height:45px">Learn More</div>
<div class="dots"><span style="left:563px"></span><span class="on" style="left:594px"></span><span style="left:625px"></span></div>

<p class="abs intro">It is a long established fact that a reader will be distracted by the readable content of a page when looking at its layout. The point of using Lorem Ipsum is that it has a more-or-less normal distribution It was popularised in the 1960s with the release of Letraset sheets containing Lorem Ipsum passages, and more recently with desktop publishing software like Aldus PageMaker including versions of Lorem Ipsum.</p>

<section class="abs who">
  <h2>Who We Are</h2>
  <p>It is a long established fact that a reader will be distracted by the readable content of a page when looking at its layout. The point of using Lorem Ipsum is that it has amore-or-less normal distribution of letters, as opposed to using 'Content here, content here', making it look like readable English.</p>
</section>
<div class="btn" style="left:93px;top:1088px;width:122px;height:45px">Learn More</div>
<div class="photo" style="left:542px;top:812px;width:341px;height:442px;background:linear-gradient(180deg,#f3e6c4 0%,#d88a4a 45%,#c2441e 75%,#6c6f6a 100%)" role="img" aria-label="Rows of orange drums beside a truck trailer"></div>
<div class="photo" style="left:883px;top:812px;width:317px;height:213px;background:linear-gradient(160deg,#cfd4d6 0%,#d9532c 50%,#b8381c 100%)" role="img" aria-label="Stacked orange barrels"></div>
<div class="photo" style="left:883px;top:1025px;width:317px;height:229px;background:linear-gradient(180deg,#b9d6ec 0%,#3c5e86 45%,#a04a3c 100%)" role="img" aria-label="Stacked shipping containers under a blue sky"></div>

<section class="abs jobs" role="img" aria-label="Truck driver in a red vest standing in front of his truck"></section>
<div class="abs jobs-text">
  <h2>Jobs</h2>
  <p>Lorem Ipsum has been the industry's standard dummy text ever since the 1500swhen an unknown printer took a galley of type and scrambled it to make a type specimen book.</p>
</div>
<div class="btn" style="left:94px;top:1773px;width:122px;height:44px">View Jobs</div>

<form class="abs apply">
  <h3>Quick Apply</h3>
  <div class="field" style="left:69px;top:67px;width:134px">First Name :</div>
  <div class="field" style="left:209px;top:67px;width:132px">Last Name :</div>
  <div class="field" style="left:69px;top:113px;width:272px">Email :</div>
  <div class="field" style="left:69px;top:159px;width:272px">Phone :</div>
  <div class="field" style="left:69px;top:205px;width:88px">City</div>
  <div class="field select" style="left:162px;top:205px;width:88px">State<span class="caret"></span></div>
  <div class="field" style="left:255px;top:205px;width:86px">Zipcode</div>
  <div class="field select" style="left:69px;top:252px;width:272px">How much driving experience have year<span class="caret"></span></div>
  <div class="field select" style="left:69px;top:298px;width:272px">How many carriers have you worked<span class="caret"></span></div>
  <div class="field select" style="left:69px;top:345px;width:272px">How many accidents have you been<span class="caret"></span></div>
  <div class="field select" style="left:69px;top:391px;width:272px">How many violations have you been<span class="caret"></span></div>
  <div class="btn upload" style="left:69px;top:441px;width:120px;height:45px">Upload Resume</div>
  <div class="btn submit" style="left:197px;top:441px;width:120px;height:45px">Submit Now</div>
</form>

<section class="abs services"></section>
<div class="card" style="left:82px">
  <div class="circle" style="background:radial-gradient(circle at 50% 45%,#4a4a4a 0%,#2e4c4c 55%,#4f7f86 100%)" role="img" aria-label="Bearded driver in a cap beside his truck"></div>
  <h3>Printing and Typesetting</h3>
  <p>long established fact that a reader will be distracted by the readable content of a page when looking at its layout. The point of using...</p>
</div>
<div class="card" style="left:439px">
  <div class="circle" style="background:linear-gradient(160deg,#9fb3c2 0%,#6f7f6a 40%,#8f8f8f 60%,#c0392b 75%,#5b6b5b 100%)" role="img" aria-label="Red tanker truck on a highway"></div>
  <h3>Printing and Typesetting</h3>
  <p>long established fact that a reader will be distracted by the readable content of a page when looking at its layout. The point of using...</p>
</div>
<div class="card" style="left:790px">
  <div class="circle" style="background:linear-gradient(180deg,#b9cfe3 0%,#6f8a6a 45%,#1e3550 70%,#8a8a80 100%)" role="img" aria-label="Vintage blue flatbed truck"></div>
  <h3>Printing and Typesetting</h3>
  <p>long established fact that a reader will be distracted by the readable content of a page when looking at its layout. The point of using...</p>
</div>
<div class="btn" style="left:540px;top:2297px;width:121px;height:45px">View Services</div>

<footer class="abs footer">
  <div class="f-brand">Meridane<small>Haulage</small></div>
  <p class="f-about">Lorem Ipsum has been the industry's standard dummy text ever since the 1500s, when an unknown printer took a galley of type and scrambled it to make a type specimen book. It has survived not only five centuries.</p>

  <div class="f-title" style="left:420px">Quick Link</div>
  <div class="f-links">
    <a style="top:158px" href="#">Home</a>
    <a style="top:203px" href="#">About</a>
    <a style="top:248px" href="#">Services</a>
    <a style="top:292px" href="#">Jobs</a>
    <a style="top:338px" href="#">Contact</a>
  </div>

  <div class="f-title" style="left:597px">Quick Contact</div>
  <div class="f-contact" style="top:154px"><b>Location :</b><br>Lorem Ipsum,north America</div>
  <div class="f-contact" style="top:218px"><b>Email :</b><br>hello@meridanehaulage.com</div>
  <div class="f-contact" style="top:281px"><b>Phone :</b><br>800 555-0147</div>

  <div class="f-title" style="left:834px">Quick Contact</div>
  <p class="f-news">long established fact that a reader will be distracted by the readable content</p>
  <div class="f-input">Enter Your Email id</div>
  <div class="btn" style="left:838px;top:262px;width:121px;height:44px">Submit Now</div>
  <div class="social"><span style="left:837px"></span><span style="left:870px"></span><span style="left:903px"></span><span style="left:935px"></span></div>

  <p class="copy">Copyright©2019 <span>meridanehaulage</span>. All Rights Reserved.</p>
</footer>

</body>
</html>
```